KDR Business Card

Keystone Draper Resources is a successful and reputable financial services company.Our main services are home loans, commercial loans, vehicle finance and equipment finance. We also do development finance for property developers. Our company is always evolving to always be an industry leader in best financial service practices with access to the largest range of lenders in the country.

We want the business card to reflect our national finance company. Modern, professional corporate image. At the same time the concept of Keystone Draper Resources is that we help build wealth for you but the process for the client is an enjoyable peaceful experience. Not stressful at all .....

Colors to be same as the logo .... gold silver black white as the options

On the reverse side of the card I wanted either just the logo symbol or the logo symbol and text of the logo ....

It could be on a black background ..... or silver or gold .... want it to be quite striking to look at when you first see the card.

On the other side of the card I wanted the following details:

Martin Haldane
Director

0438 927 604

martin@kdrgrp.com.au

Po Box 718
Ferndale ACT 2614

www.kdrgrp.com.au

ACN 618 204 957 (This can be in very small print and can be in the bottom corner of the card or somewhere not very prominent)

As requested Ive uploaded the logo file in both .ai and .pdf formats. Please let me know if you need anything else. Thanks

Reason: Still deciding on which design I like best. I will provide individual feedback as well.

```html
<!DOCTYPE html>
<html lang="en">
<head>
<meta charset="utf-8">
<title>KDR Business Card</title>
<link rel="stylesheet" href="https://fonts.googleapis.com/css2?family=Noto+Serif:wght@400&display=swap">
<style>
  :root {
    --page: #ffffff;
    --card-black: #121212;
    --card-black-deep: #070707;
    --band-black: #050505;
    --gold: #c9a43a;
    --gold-light: #e6c965;
    --silver: #a9a9a9;
    --silver-dim: #8a8a8a;
    --divider: #5a5a5a;
  }
  * { box-sizing: border-box; margin: 0; padding: 0; }
  html, body {
    width: 1200px;
    height: 800px;
    overflow: hidden;
    background: var(--page);
  }
  .stage {
    position: relative;
    width: 1200px;
    height: 800px;
    display: flex;
    align-items: center;
    justify-content: center;
    gap: 40px;
    font-family: "Noto Serif", Georgia, serif;
  }
  .card {
    position: relative;
    width: 540px;
    height: 310px;
    border-radius: 3px;
    overflow: hidden;
    background: radial-gradient(ellipse at 40% 35%, #1e1e1e 0%, var(--card-black) 45%, var(--card-black-deep) 100%);
    box-shadow: 0 6px 18px rgba(0,0,0,0.25);
  }

  /* Front: details side */
  .band {
    position: absolute;
    left: 0;
    right: 0;
    top: 78px;
    height: 160px;
    background: var(--band-black);
    border-top: 4px solid var(--gold);
    border-bottom: 4px solid var(--gold);
  }
  .identity {
    position: absolute;
    left: 26px;
    top: 22px;
    width: 250px;
  }
  .brand {
    display: flex;
    align-items: center;
    gap: 10px;
  }
  .brand-mark {
    width: 30px;
    height: 30px;
    flex: none;
    border: 2px solid var(--gold);
    border-radius: 50%;
  }
  .brand-name {
    color: var(--gold);
    font-size: 13px;
    letter-spacing: 1.5px;
    text-transform: uppercase;
    line-height: 1.3;
  }
  .person {
    margin-top: 22px;
    color: var(--silver-dim);
    text-transform: uppercase;
  }
  .person-name {
    font-size: 19px;
    letter-spacing: 1.5px;
    line-height: 1.1;
  }
  .person-title {
    font-size: 12px;
    letter-spacing: 1px;
    margin-top: 4px;
  }
  .divider {
    position: absolute;
    left: 290px;
    top: 16px;
    bottom: 16px;
    width: 1px;
    background: var(--divider);
  }
  .contacts {
    position: absolute;
    left: 306px;
    top: 24px;
    list-style: none;
    color: var(--silver);
    font-size: 13.5px;
    line-height: 1;
  }
  .contacts li {
    display: flex;
    align-items: center;
    gap: 9px;
    height: 27px;
    white-space: nowrap;
  }
  .contact-icon {
    width: 12px;
    height: 12px;
    flex: none;
  }

  /* Back: brand side */
  .brand-large {
    position: absolute;
    left: 70px;
    top: 70px;
  }
  .brand-large .brand-mark {
    width: 92px;
    height: 92px;
    border-width: 5px;
    border-color: var(--gold-light);
  }
  .brand-large .brand-name {
    margin-top: 14px;
    font-size: 30px;
    letter-spacing: 3px;
    line-height: 1.2;
    color: var(--gold-light);
  }
</style>
</head>
<body>
<main class="stage">

  <section class="card card-front" aria-label="Business card, details side">
    <div class="band">
      <div class="identity">
        <div class="brand">
          <span class="brand-mark"></span>
          <span class="brand-name">Keystone Draper Resources</span>
        </div>
        <div class="person">
          <p class="person-name">Martin Haldane</p>
          <p class="person-title">Owner</p>
        </div>
      </div>

      <span class="divider"></span>

      <ul class="contacts">
        <li>
          <svg class="contact-icon" viewBox="0 0 12 12" aria-hidden="true">
            <rect x="3" y="0.5" width="6" height="11" rx="1.2" fill="none" stroke="#8a8a8a" stroke-width="1.2"/>
            <circle cx="6" cy="9.5" r="0.7" fill="#8a8a8a"/>
          </svg>
          0438 927 604
        </li>
        <li>
          <svg class="contact-icon" viewBox="0 0 12 12" aria-hidden="true">
            <rect x="0.6" y="2.5" width="10.8" height="7" rx="0.8" fill="none" stroke="#8a8a8a" stroke-width="1.2"/>
            <path d="M0.8 3 L6 7 L11.2 3" fill="none" stroke="#8a8a8a" stroke-width="1.2"/>
          </svg>
          martin@kdrgrp.com.au
        </li>
        <li>
          <svg class="contact-icon" viewBox="0 0 12 12" aria-hidden="true">
            <path d="M6 11.5 C3.5 8 2 6.2 2 4.2 A4 4 0 0 1 10 4.2 C10 6.2 8.5 8 6 11.5 Z" fill="#8a8a8a"/>
            <circle cx="6" cy="4.3" r="1.5" fill="#050505"/>
          </svg>
          Po Box 718 Ferndale ACT 2614
        </li>
        <li>
          <svg class="contact-icon" viewBox="0 0 12 12" aria-hidden="true">
            <circle cx="6" cy="6" r="5.2" fill="none" stroke="#8a8a8a" stroke-width="1.1"/>
            <ellipse cx="6" cy="6" rx="2.3" ry="5.2" fill="none" stroke="#8a8a8a" stroke-width="1"/>
            <line x1="0.8" y1="6" x2="11.2" y2="6" stroke="#8a8a8a" stroke-width="1"/>
          </svg>
          www.kdrgrp.com.au
        </li>
      </ul>
    </div>
  </section>

  <section class="card card-back" aria-label="Business card, brand side">
    <div class="brand-large">
      <span class="brand-mark"></span>
      <p class="brand-name">Keystone Draper<br>Resources</p>
    </div>
  </section>

</main>
</body>
</html>
```